Fahrzeugbeschriftung für neuen Veltaro Sirenza Kombi
Zielgruppe
Hersteller und Installateur von Fussbodenheizungen mit niedrigem Aufbau speziell für Umbau und Rennovationen. Hauseigene wassergeführte Systeme (Lumba K und Lumba eco) sowie auch elektroheizmatten.
Weitere Details auf www.plavexhaus.ch
Zielgruppe sind meistens private Bauherren, aber auch Architekten, Planer & Sanitärfirmen
Aufgabenstellung
Unser Markenzeichen sind die zwei roten Füsse als Symbol für warme Füsse. Logo im Anhang.
Die neue Beschriftung soll moderner und jünger daher kommen aber trotzdem mit Stil.
Fahrzeugfarbe schwarz oder weiss.

```html
<!DOCTYPE html>
<html lang="de">
<head>
<meta charset="utf-8">
<title>Plavexhaus Fahrzeugbeschriftung</title>
<link rel="stylesheet" href="https://fonts.googleapis.com/css2?family=Open+Sans:wght@400;600;700&display=swap">
<style>
  :root {
    --bg: #ececec;
    --body-light: #ffffff;
    --body-shade: #d9d9d9;
    --brand-red: #e5343a;
    --soft-red: #f0676b;
    --dark-red: #c9202a;
    --ink: #2f2f2f;
    --ink-soft: #555555;
  }
  html, body {
    margin: 0;
    padding: 0;
    width: 1200px;
    height: 653px;
    overflow: hidden;
    background: var(--bg);
  }
  .wrap-design {
    display: block;
    width: 1200px;
    height: 653px;
    font-family: "Open Sans", Arial, sans-serif;
  }
  .vehicle-body { fill: url(#bodyShade); }
  .swoosh { fill: var(--brand-red); }
  .swoosh--rear { fill: var(--dark-red); }
  .services text { fill: var(--brand-red); font-size: 21px; font-weight: 600; }
  .services .service--first { fill: var(--soft-red); }
  .web { fill: var(--dark-red); font-size: 16px; font-weight: 700; }
  .tagline { fill: var(--ink-soft); font-size: 18px; font-weight: 400; }
  .brand-name { fill: var(--ink); font-size: 48px; font-weight: 700; }
  .brand-mark { fill: var(--brand-red); }
  .phone { fill: var(--brand-red); font-size: 25px; font-weight: 700; }
</style>
</head>
<body>
<svg class="wrap-design" viewBox="0 0 1417 771" xmlns="http://www.w3.org/2000/svg" aria-label="Fahrzeugbeschriftung Plavexhaus, flach dargestellt">
  <defs>
    <linearGradient id="bodyShade" x1="0" y1="0" x2="0" y2="1">
      <stop offset="0" stop-color="var(--body-shade)"/>
      <stop offset="0.35" stop-color="var(--body-light)"/>
      <stop offset="1" stop-color="var(--body-shade)"/>
    </linearGradient>
  </defs>

  <!-- Vehicle side as a plain area -->
  <path class="vehicle-body" role="img" aria-label="Seitenansicht des weissen Kombis als Träger der Beschriftung"
        d="M96,470 C96,420 104,360 120,320 C150,270 200,230 260,212 C360,196 600,188 760,196 C860,220 950,280 1010,312 C1120,330 1240,350 1280,380 C1300,400 1312,470 1310,520 C1306,540 1290,548 1270,548 L100,548 C96,530 96,500 96,470 Z"/>

  <!-- Rear side swoosh -->
  <path class="swoosh swoosh--rear" d="M130,458 C230,432 300,396 385,404 L381,413 C305,412 258,448 238,472 C200,472 160,467 130,458 Z"/>
  <!-- Sill line rising to front wheel arch -->
  <path class="swoosh" d="M470,468 L968,486 C988,458 1004,434 1030,419 L1027,427 C1011,446 996,474 982,497 L470,474 Z"/>
  <!-- Front bumper accent -->
  <path class="swoosh" d="M1218,473 L1229,470 L1241,518 L1231,520 Z"/>

  <!-- Service list -->
  <g class="services">
    <text class="service--first" x="407" y="396">Ausstellung</text>
    <text x="437" y="419">Beratung</text>
    <text x="475" y="443">Verkauf</text>
    <text x="510" y="465">Installation</text>
  </g>

  <!-- Web address -->
  <text class="web" x="790" y="357" textLength="160" lengthAdjust="spacingAndGlyphs">www.plavexhaus.ch</text>

  <!-- Brand block -->
  <text class="tagline" x="678" y="414" textLength="236" lengthAdjust="spacingAndGlyphs">Die Profis für Bodenwärme</text>
  <rect class="brand-mark" x="930" y="388" width="38" height="38"/>
  <text class="brand-name" x="676" y="466" textLength="282" lengthAdjust="spacingAndGlyphs">Plavexhaus</text>

  <!-- Phone number -->
  <text class="phone" x="1032" y="402" transform="rotate(14 1032 402)" textLength="192" lengthAdjust="spacingAndGlyphs">9876 5432 111</text>
</svg>
</body>
</html>
```